Brell Harbor Company Business Cards

Front and Back Business Card - logo and text setup - cool design. I need workable photoshop or illustrator files so I can setup each employee card with design that is created
Updates

Hi everyone, thank you for the great entries. Please no more white and blue cards - there are so many already - black and silver only now please. thanks!

Target Market(s)

Construction Industry - Facility Managers

Industry/Entity Type

Construction

Contact Information for Business Card

I really like contemporary simplistic looks - clean neat....not opposed to seeing some black backrounds

Requirements
Must have
• Logo/website address with design on front only - www.brellharbor-example.com (logo attached)
• Back:
• Name/Title/Company Address/Phone/email address
Nice to have
• Cool design
Should not have
• Nothing gimmicky like Fire or Water - since we are a Fire Protection company - it has all been done

```html
<!DOCTYPE html>
<html lang="en">
<head>
<meta charset="utf-8">
<title>Brell Harbor Company Business Cards</title>
<link rel="stylesheet" href="https://fonts.googleapis.com/css2?family=Arimo:wght@400;700&family=Jost:wght@600;700&display=swap">
<style>
  :root {
    --page: #f2f2f2;
    --silver: #c4c8cd;
    --silver-light: #e4e6e9;
    --silver-dark: #9aa0a7;
    --black: #141416;
    --ink: #1a1a1c;
  }
  * { margin: 0; padding: 0; box-sizing: border-box; }
  html, body { width: 1200px; height: 1200px; overflow: hidden; }
  body { background: var(--page); position: relative; font-family: "Arimo", Arial, sans-serif; }

  .card { position: absolute; left: 222px; width: 754px; border-radius: 16px; overflow: hidden; }

  .card-front {
    top: 128px; height: 428px;
    background: linear-gradient(135deg, var(--silver-light) 0%, var(--silver) 55%, var(--silver-dark) 100%);
  }
  .brand-name {
    position: absolute; left: 0; right: 0; top: 172px;
    text-align: center; font-weight: 700;
    font-size: 62px; letter-spacing: -1px; line-height: 1; color: var(--ink);
  }
  .website {
    position: absolute; left: 0; right: 0; top: 360px;
    text-align: center; font-size: 22px; line-height: 1.2; color: var(--ink);
  }

  .card-back { top: 608px; height: 424px; background: var(--black); }
  .name-tab {
    position: absolute; left: 0; top: 184px; width: 284px; height: 56px;
    background: var(--silver); border-radius: 0 8px 8px 0;
    text-align: center; color: var(--ink); font-family: "Jost", "Futura", sans-serif;
    padding-right: 12px;
  }
  .person-name { display: block; font-weight: 700; font-size: 29px; line-height: 1; padding-top: 8px; }
  .person-title { display: block; font-weight: 600; font-size: 13px; line-height: 1.2; margin-top: 3px; }

  .contact-list { position: absolute; left: 384px; top: 146px; list-style: none; }
  .contact-item { display: flex; align-items: center; height: 29px; margin-bottom: 23px; }
  .contact-icon { width: 29px; height: 29px; flex: none; }
  .contact-text { margin-left: 29px; font-size: 19px; line-height: 1; color: var(--silver-light); }

  .edge-tab { position: absolute; right: 0; top: 154px; width: 12px; height: 118px; background: var(--silver); border-radius: 6px 0 0 6px; }
  .base-band { position: absolute; left: 0; right: 0; top: 376px; height: 21px; background: var(--silver); }
</style>
</head>
<body>
  <section class="card card-front">
    <div class="brand-name">Brell Harbor</div>
    <div class="website">www.brellharbor-example.com</div>
  </section>

  <section class="card card-back">
    <div class="name-tab">
      <span class="person-name">YOUR name</span>
      <span class="person-title">Title</span>
    </div>

    <ul class="contact-list">
      <li class="contact-item">
        <svg class="contact-icon" viewBox="0 0 30 30" aria-hidden="true">
          <circle cx="15" cy="15" r="15" fill="#c4c8cd"/>
          <path d="M8 15 L15 8.5 L22 15 M10 13.5 V21.5 H20 V13.5 M13.5 21.5 V17 H16.5 V21.5" fill="none" stroke="#141416" stroke-width="1.6" stroke-linejoin="round"/>
        </svg>
        <span class="contact-text">Company Address</span>
      </li>
      <li class="contact-item">
        <svg class="contact-icon" viewBox="0 0 30 30" aria-hidden="true">
          <circle cx="15" cy="15" r="15" fill="#c4c8cd"/>
          <path d="M10 8 L12.5 8 L14 11.5 L12.3 13 C13.2 15 15 16.8 17 17.7 L18.5 16 L22 17.5 L22 20 C22 21 21 22 20 22 C14 21.5 8.5 16 8 10 C8 9 9 8 10 8 Z" fill="none" stroke="#141416" stroke-width="1.6" stroke-linejoin="round"/>
        </svg>
        <span class="contact-text">123456789</span>
      </li>
      <li class="contact-item">
        <svg class="contact-icon" viewBox="0 0 30 30" aria-hidden="true">
          <circle cx="15" cy="15" r="15" fill="#c4c8cd"/>
          <rect x="8" y="10" width="14" height="10" rx="1" fill="none" stroke="#141416" stroke-width="1.6"/>
          <path d="M8 10.5 L15 16 L22 10.5" fill="none" stroke="#141416" stroke-width="1.6" stroke-linejoin="round"/>
        </svg>
        <span class="contact-text">info@brellharbor-example.com</span>
      </li>
    </ul>

    <div class="edge-tab"></div>
    <div class="base-band"></div>
  </section>
</body>
</html>
```